Lena Corvell Business Card

I need a business card that reflects my current website: itslenacorvell.example and screenshot attached. If we keep the color scheme of the site and sample card below that would be ideal. The business card should include the information on the attached sample cards.

Industry/Entity Type

Business

```html
<!DOCTYPE html>
<html lang="en">
<head>
<meta charset="utf-8">
<title>Lena Corvell Business Card</title>
<link rel="stylesheet" href="https://fonts.googleapis.com/css2?family=Arimo:wght@400&family=Kaushan+Script&display=swap">
<style>
  :root {
    --backdrop: #e9ecea;
    --mint: #86bcaa;
    --teal: #1f97a3;
    --paper: #ffffff;
    --ink: #1c1c1c;
    --ink-soft: #2c2c2c;
    --light-text: #ffffff;
  }
  * { box-sizing: border-box; margin: 0; padding: 0; }
  html, body {
    width: 1119px; height: 1200px; overflow: hidden;
    background: var(--backdrop);
  }
  .sheet { position: relative; width: 1119px; height: 1200px; }

  .card {
    position: absolute;
    width: calc(350 * var(--u));
    height: calc(200 * var(--u));
    font-size: var(--u);
    background: var(--mint);
    overflow: hidden;
    box-shadow: 0 6px 18px rgba(0,0,0,.18);
    font-family: "Arimo", Arial, sans-serif;
    color: var(--light-text);
  }
  .card--hero { --u: 2.743px; left: 79.5px; top: 193px; }
  .card--small { --u: 0.971px; top: 812px; border-radius: 6px; }
  .card--curve { left: 30px; }
  .card--wave { left: 390px; }
  .card--arc { left: 750px; }

  .card__shape { position: absolute; inset: 0; width: 100%; height: 100%; }
  .shape-paper { fill: var(--paper); }
  .shape-band { fill: var(--teal); }

  .card__name {
    position: absolute;
    left: calc(60 * var(--u));
    top: calc(22 * var(--u));
    font-family: "Arimo", Arial, sans-serif;
    font-size: calc(17 * var(--u));
    line-height: 1;
    color: var(--ink);
    letter-spacing: 0.01em;
    white-space: nowrap;
  }
  .card--wave .card__name,
  .card--arc .card__name {
    left: 50%;
    transform: translateX(-50%);
    top: calc(24 * var(--u));
  }
  .card--arc .card__name { top: calc(26 * var(--u)); }

  .card__details { position: absolute; left: 20em; top: 90em; }
  .card__tagline {
    font-family: "Kaushan Script", cursive;
    font-size: 9.6em;
    white-space: nowrap;
  }
  .card__line {
    display: flex; align-items: center; gap: 3em;
    font-size: 1em; margin-top: 6em; white-space: nowrap;
  }
  .card__line span { font-size: 8.6em; }
  .card__line .card__web { font-size: 9.4em; }
  .icon-phone { width: 7em; height: 7em; fill: currentColor; }
  .icon-square {
    width: 8.5em; height: 8.5em; border-radius: 1.5em;
    background: var(--teal);
  }

  .card--arc .card__details {
    left: 50%; transform: translateX(-50%); top: 97em; color: var(--ink-soft);
  }
  .card--arc .icon-square { background: var(--ink-soft); }
</style>
</head>
<body>
<main class="sheet">

  <article class="card card--hero">
    <svg class="card__shape" viewBox="0 0 350 200" preserveAspectRatio="none" aria-hidden="true">
      <path class="shape-band" d="M252 0 H292 C286 52 236 78 150 72 C212 64 246 42 252 0 Z"/>
      <path class="shape-paper" d="M0 0 H258 C252 42 214 64 150 66 L0 66 Z"/>
    </svg>
    <p class="card__name">Lena Corvell</p>
    <div class="card__details">
      <p class="card__tagline">Brand Curator ★ Digital Storyteller ★ Social Entrepreneur</p>
      <p class="card__line"><span>me@lenacorvell.example</span>
        <svg class="icon-phone" viewBox="0 0 24 24" aria-hidden="true"><path d="M6.6 10.8a15 15 0 0 0 6.6 6.6l2.2-2.2a1 1 0 0 1 1-.25 11.4 11.4 0 0 0 3.6.57 1 1 0 0 1 1 1V20a1 1 0 0 1-1 1A17 17 0 0 1 3 4a1 1 0 0 1 1-1h3.5a1 1 0 0 1 1 1c0 1.25.2 2.45.57 3.57a1 1 0 0 1-.25 1z"/></svg>
        <span>555.010.4427</span></p>
      <p class="card__line"><i class="icon-square"></i><span>@itslenacorvell</span></p>
      <p class="card__line"><span class="card__web">itslenacorvell.example</span></p>
    </div>
  </article>

  <article class="card card--small card--curve">
    <svg class="card__shape" viewBox="0 0 350 200" preserveAspectRatio="none" aria-hidden="true">
      <path class="shape-band" d="M252 0 H292 C286 52 236 78 150 72 C212 64 246 42 252 0 Z"/>
      <path class="shape-paper" d="M0 0 H258 C252 42 214 64 150 66 L0 66 Z"/>
    </svg>
    <p class="card__name">Lena Corvell</p>
    <div class="card__details">
      <p class="card__tagline">Brand Curator • Digital Storyteller • Social Entrepreneur</p>
      <p class="card__line"><span>me@lenacorvell.example</span>
        <svg class="icon-phone" viewBox="0 0 24 24" aria-hidden="true"><path d="M6.6 10.8a15 15 0 0 0 6.6 6.6l2.2-2.2a1 1 0 0 1 1-.25 11.4 11.4 0 0 0 3.6.57 1 1 0 0 1 1 1V20a1 1 0 0 1-1 1A17 17 0 0 1 3 4a1 1 0 0 1 1-1h3.5a1 1 0 0 1 1 1c0 1.25.2 2.45.57 3.57a1 1 0 0 1-.25 1z"/></svg>
        <span>555.010.4427</span></p>
      <p class="card__line"><i class="icon-square"></i><span>@itslenacorvell</span></p>
      <p class="card__line"><span class="card__web">itslenacorvell.example</span></p>
    </div>
  </article>

  <article class="card card--small card--wave">
    <svg class="card__shape" viewBox="0 0 350 200" preserveAspectRatio="none" aria-hidden="true">
      <path class="shape-band" d="M0 66 C70 70 130 82 200 80 C260 78 300 62 350 58 V70 C300 72 262 86 200 87 C128 88 70 78 0 76 Z"/>
      <path class="shape-paper" d="M0 0 H350 V58 C300 62 260 78 200 80 C130 82 70 70 0 66 Z"/>
    </svg>
    <p class="card__name">Lena Corvell</p>
    <div class="card__details">
      <p class="card__tagline">Brand Curator • Digital Storyteller • Social Entrepreneur</p>
      <p class="card__line"><span>me@lenacorvell.example</span>
        <svg class="icon-phone" viewBox="0 0 24 24" aria-hidden="true"><path d="M6.6 10.8a15 15 0 0 0 6.6 6.6l2.2-2.2a1 1 0 0 1 1-.25 11.4 11.4 0 0 0 3.6.57 1 1 0 0 1 1 1V20a1 1 0 0 1-1 1A17 17 0 0 1 3 4a1 1 0 0 1 1-1h3.5a1 1 0 0 1 1 1c0 1.25.2 2.45.57 3.57a1 1 0 0 1-.25 1z"/></svg>
        <span>555.010.4427</span></p>
      <p class="card__line"><i class="icon-square"></i><span>@itslenacorvell</span></p>
      <p class="card__line"><span class="card__web">itslenacorvell.example</span></p>
    </div>
  </article>

  <article class="card card--small card--arc">
    <svg class="card__shape" viewBox="0 0 350 200" preserveAspectRatio="none" aria-hidden="true">
      <path class="shape-band" d="M0 78 C60 82 120 88 180 86 C250 84 300 72 350 60 V70 C300 84 250 94 180 95 C115 96 55 90 0 86 Z"/>
      <path class="shape-paper" d="M0 0 H350 V60 C300 72 250 84 180 86 C120 88 60 82 0 78 Z"/>
    </svg>
    <p class="card__name">Lena Corvell</p>
    <div class="card__details">
      <p class="card__tagline">Brand Curator • Digital Storyteller • Social Entrepreneur</p>
      <p class="card__line"><span>me@lenacorvell.example</span>
        <svg class="icon-phone" viewBox="0 0 24 24" aria-hidden="true"><path d="M6.6 10.8a15 15 0 0 0 6.6 6.6l2.2-2.2a1 1 0 0 1 1-.25 11.4 11.4 0 0 0 3.6.57 1 1 0 0 1 1 1V20a1 1 0 0 1-1 1A17 17 0 0 1 3 4a1 1 0 0 1 1-1h3.5a1 1 0 0 1 1 1c0 1.25.2 2.45.57 3.57a1 1 0 0 1-.25 1z"/></svg>
        <span>555.010.4427</span></p>
      <p class="card__line"><i class="icon-square"></i><span>@itslenacorvell</span></p>
      <p class="card__line"><span class="card__web">itslenacorvell.example</span></p>
    </div>
  </article>

</main>
</body>
</html>
```